Small rum distillery looking for bottle design

Small rum distillery in Estonia. Looking for bottle lable design. It should be simple but at the same time point out from the variety of other bottles.
As we are a small nordic country, design can be some how nordic or represent our country. It can also have some connection with sailing or sea as we know it pirates love it.
Bottle we are using is Corvane 540

Industry/Entity Type

food and beverage

Other font styles liked:
• Baskerville

```html
<!DOCTYPE html>
<html lang="en">
<head>
<meta charset="utf-8">
<title>Varde Distillery – Rum Label</title>
<link rel="stylesheet" href="https://fonts.googleapis.com/css2?family=EB+Garamond:wght@400;500;600&display=swap">
<style>
  :root {
    --backdrop: #efefef;
    --cream: #f8f9f3;
    --gold-deep: #b47d20;
    --gold-mid: #c8993c;
    --gold-light: #d8b46a;
    --ink: #474443;
    --bottle-red: #f50d0d;
    --white: #ffffff;
  }
  html, body {
    margin: 0;
    padding: 0;
    width: 1200px;
    height: 1200px;
    overflow: hidden;
    background: var(--backdrop);
  }
  .artboard {
    display: block;
    width: 1200px;
    height: 1200px;
  }
  .label-type {
    font-family: "EB Garamond", "Libre Baskerville", serif;
    fill: var(--ink);
  }
  .arc-tagline { font-size: 50px; letter-spacing: 3px; }
  .edition { font-size: 56px; }
  .brand-name { font-size: 124px; font-weight: 500; letter-spacing: 6px; }
  .brand-sub { font-size: 40px; letter-spacing: 21px; }
  .origin { font-size: 19px; font-weight: 600; fill: var(--white); letter-spacing: 1.5px; }
  .neck-name {
    font-family: "EB Garamond", "Libre Baskerville", serif;
    font-size: 38px;
    letter-spacing: 3px;
    fill: var(--white);
  }
</style>
</head>
<body>
<svg class="artboard" viewBox="0 0 1932 1932" xmlns="http://www.w3.org/2000/svg">
  <defs>
    <linearGradient id="gold-ring" x1="0" y1="0" x2="0" y2="1">
      <stop offset="0" stop-color="#b98324"/>
      <stop offset="1" stop-color="#d6b268"/>
    </linearGradient>
    <linearGradient id="gold-fill" x1="0" y1="0" x2="0" y2="1">
      <stop offset="0" stop-color="#b07a1c"/>
      <stop offset="1" stop-color="#d9b874"/>
    </linearGradient>
    <linearGradient id="sea-fill" x1="0" y1="0" x2="0" y2="1">
      <stop offset="0" stop-color="#b8842a"/>
      <stop offset="1" stop-color="#e6d2a2"/>
    </linearGradient>
    <clipPath id="ring-clip">
      <path d="M200,840 C200,640 360,503 538,503 C716,503 880,640 880,840 V1030 C880,1220 730,1366 538,1366 C346,1366 196,1220 196,1030 Z"/>
    </clipPath>
    <path id="tagline-arc" d="M273,820 A265,265 0 0 1 803,820"/>

    <g id="front-label">
      <path class="label-base" fill="var(--cream)"
        d="M170,840 C170,620 340,478 538,478 C736,478 907,620 907,840 V1030 C907,1230 740,1392 538,1392 C336,1392 170,1230 170,1030 Z"/>
      <g class="label-sea" clip-path="url(#ring-clip)">
        <rect x="290" y="1255" width="495" height="120" fill="url(#sea-fill)"
          role="img" aria-label="Engraved sea with horizontal wave lines"/>
      </g>
      <path class="label-ring" fill="none" stroke="url(#gold-ring)" stroke-width="11"
        d="M200,840 C200,640 360,503 538,503 C716,503 880,640 880,840 V1030 C880,1220 730,1366 538,1366 C346,1366 196,1220 196,1030 Z"/>
      <path class="inner-arc" fill="none" stroke="url(#gold-ring)" stroke-width="7"
        d="M320,694 C280,750 257,830 257,935 C257,1040 280,1118 320,1173"/>
      <path class="inner-arc" fill="none" stroke="url(#gold-ring)" stroke-width="7"
        d="M756,694 C796,750 819,830 819,935 C819,1040 796,1118 756,1173"/>
      <path class="arc-point" fill="var(--gold-mid)" d="M235,935 L255,918 L255,952 Z"/>
      <path class="arc-point" fill="var(--gold-mid)" d="M841,935 L821,918 L821,952 Z"/>

      <text class="label-type arc-tagline" text-anchor="middle">
        <textPath href="#tagline-arc" startOffset="50%">PREMIUM QUALITY</textPath>
      </text>
      <text class="label-type edition" x="538" y="666" text-anchor="middle">№.1</text>

      <circle class="brand-mark" cx="538" cy="802" r="62" fill="var(--ink)"/>

      <text class="label-type brand-name" x="538" y="995" text-anchor="middle">VARDE</text>
      <rect class="brand-rule" x="300" y="1021" width="476" height="5" fill="var(--ink)"/>
      <text class="label-type brand-sub" x="548" y="1077" text-anchor="middle">DISTILLERY</text>

      <rect class="ship-art" x="435" y="1105" width="226" height="182" rx="14" fill="url(#gold-fill)"
        role="img" aria-label="Viking longship with a striped sail and oars on the sea"/>

      <text class="label-type origin" x="538" y="1330" text-anchor="middle">ESTONIA</text>
      <text class="label-type origin" x="538" y="1346" text-anchor="middle" style="font-size:15px">MADE</text>
    </g>
  </defs>

  <!-- Flat front label -->
  <use href="#front-label"/>

  <!-- Bottle mockup -->
  <g class="bottle">
    <path class="bottle-outline" fill="none" stroke="var(--bottle-red)" stroke-width="7"
      d="M1328,522 H1450 q8,0 8,8 V562 q0,8 -6,10 V710 q0,25 22,38 L1512,766 Q1570,796 1572,872 V1325 q0,20 -20,20 H1228 q-20,0 -20,-20 V872 Q1210,796 1268,766 L1306,748 q22,-13 22,-38 V572 q-6,-2 -6,-10 V530 q0,-8 8,-8 Z"/>

    <rect class="neck-strip" x="1361" y="527" width="57" height="159" fill="url(#gold-fill)"/>
    <text class="neck-name" transform="translate(1402 607) rotate(-90)" text-anchor="middle">VARDE</text>

    <rect class="body-band" x="1038" y="929" width="702" height="212" fill="var(--cream)"/>
    <rect class="band-pattern" x="1040" y="965" width="192" height="140" fill="#e2c992"
      role="img" aria-label="Gold chevron wave pattern"/>
    <rect class="band-pattern" x="1546" y="965" width="192" height="140" fill="#e2c992"
      role="img" aria-label="Gold chevron wave pattern"/>

    <use href="#front-label" transform="translate(1143.7 608.6) scale(0.456)"/>
  </g>
</svg>
</body>
</html>
```